Security Officer Training Certifications POSTCARD

We need Post Card Design
-Front and Back
-In Compliance with MERLO PRESS for upload!
-For Oversized and Jumbo Size Cards (merlo presses)
Our Company:
www.brandelhollowacademy.org (FOR IDEAS)
We provide Corporate Security Officer/Criminal Justice/Police Tactics Training for Private Companies that have a security department and officers.
We provide:
Handcuffing certifications
Pepper Spray
Compliance Training
Instructor Training
California Guard Card
Our Card to display powerful image for a Security Officer Department
Traits in Pic and Deigns
VALUE
COMPETITIVE EDGE
PROFESSIONAL GROWTH
QUALITY
PROFICIENT/EFFECTIVE SECURITY OFFICERS
TACTICAL OFFICERS
PROFESSIONALISM
EXPERTS
INDUSTRY LEADERS
READINESS
FRONT DESIGN TO BE VERY CATCH AND ATTRACTIVE!
-Please put the images of lawn enforcement, security guards, public safety department in the FRONT
BACK OF THE CARD DESIGN
-Please put our Services/Menu, CREATIVE and CATCHY, in columns and with vivid colors.

```html
<!DOCTYPE html>
<html lang="en">
<head>
<meta charset="utf-8">
<title>Brandel Hollow Academy – Postcard</title>
<link href="https://fonts.googleapis.com/css2?family=Ubuntu:wght@400;500&family=Roboto:wght@500;700&display=swap" rel="stylesheet">
<style>
  :root {
    --backdrop: #3d3d3f;
    --card: #ffffff;
    --navy: #2e3192;
    --navy-deep: #262a7e;
    --sky: #1e8fe0;
    --red: #e21b23;
    --ink: #111111;
    --photo-cool: #8c949b;
    --photo-warm: #5d5a4a;
  }
  * { margin: 0; padding: 0; box-sizing: border-box; }
  html, body { width: 860px; height: 1200px; overflow: hidden; }
  body {
    background: var(--backdrop);
    font-family: "Ubuntu", sans-serif;
    position: relative;
  }
  .postcard {
    position: absolute;
    left: 46px; top: 89px;
    width: 767px; height: 1022px;
    background: linear-gradient(200deg, #ffffff 55%, #e6e6ea 100%);
    overflow: hidden;
  }
  .hero {
    position: absolute; left: 0; top: 0;
    width: 767px; height: 511px;
  }
  .academy-name {
    position: absolute;
    left: 272px; top: 70px; width: 176px;
    text-align: center;
    font-family: "Ubuntu", sans-serif;
    font-weight: 500;
    font-size: 22px;
    line-height: 1.15;
    color: #ffffff;
    letter-spacing: 1px;
  }
  .intro {
    position: absolute; left: 0; top: 511px;
    width: 409px; height: 124px;
    background: var(--navy);
    border-bottom-right-radius: 24px;
    color: #fff;
    font-size: 15.5px;
    line-height: 19.5px;
    padding: 33px 20px 0 29px;
  }
  .services {
    position: absolute; left: 17px; top: 656px;
    list-style: none;
  }
  .services li {
    display: flex; align-items: center;
    height: 25.5px;
    color: var(--red);
    font-size: 21px;
  }
  .services svg { width: 27px; height: 12px; margin-right: 10px; flex: none; }
  .traits {
    position: absolute; left: 17px; top: 795px;
    width: 392px; height: 136px;
    background: var(--navy);
    border-radius: 22px;
    display: flex;
    padding: 17px 0 0 14px;
  }
  .traits ul {
    list-style: none;
    color: #fff;
    font-size: 13.5px;
    line-height: 17px;
    text-transform: uppercase;
  }
  .traits li { position: relative; padding-left: 21px; }
  .traits li::before {
    content: ""; position: absolute; left: 0; top: 7px;
    width: 3px; height: 3px; border-radius: 50%; background: #fff;
  }
  .traits .col-a { width: 206px; }
  .contact {
    position: absolute; left: 29px; top: 958px;
    font-family: "Roboto", sans-serif;
    color: var(--navy);
    font-weight: 700;
    font-size: 15.5px;
    line-height: 18px;
  }
  .contact .web { font-weight: 500; font-size: 13px; line-height: 17px; }
  .stamp {
    position: absolute; left: 617px; top: 560px;
    width: 96px; height: 96px;
    border: 2px solid var(--ink);
  }
  .address-line {
    position: absolute; left: 435px; width: 277px;
    height: 0; border-top: 1.5px solid var(--ink);
  }
  .partners { position: absolute; left: 440px; top: 921px; }
</style>
</head>
<body>
  <main class="postcard">
    <svg class="hero" viewBox="0 0 767 511" xmlns="http://www.w3.org/2000/svg">
      <defs>
        <linearGradient id="heroBlue" x1="0" y1="0" x2="1" y2="1">
          <stop offset="0" stop-color="#1f5fd0"/>
          <stop offset="0.5" stop-color="#2e3192"/>
          <stop offset="1" stop-color="#1e8fe0"/>
        </linearGradient>
        <linearGradient id="photoLeft" x1="0" y1="0" x2="0" y2="1">
          <stop offset="0" stop-color="#b9bfc4"/>
          <stop offset="0.5" stop-color="#5d6470"/>
          <stop offset="1" stop-color="#1f2230"/>
        </linearGradient>
        <linearGradient id="photoRight" x1="0" y1="0" x2="0" y2="1">
          <stop offset="0" stop-color="#6b6a58"/>
          <stop offset="0.55" stop-color="#3a3a30"/>
          <stop offset="1" stop-color="#16171a"/>
        </linearGradient>
        <linearGradient id="edgeSky" x1="0" y1="0" x2="0" y2="1">
          <stop offset="0" stop-color="#2e3192"/>
          <stop offset="1" stop-color="#1ea3ef"/>
        </linearGradient>
      </defs>
      <rect width="767" height="511" fill="url(#heroBlue)"/>
      <polygon points="0,185 112,511 0,511" fill="url(#edgeSky)"/>
      <polygon points="671,0 767,0 767,327" fill="url(#edgeSky)"/>
      <polygon points="0,0 215,0 378,511 112,511 0,185" fill="url(#photoLeft)"
               role="img" aria-label="Photo of an armed security officer with glasses on duty at a street checkpoint"/>
      <polygon points="215,0 671,0 767,327 767,511 378,511" fill="url(#photoRight)"
               role="img" aria-label="Photo of a uniformed security officer in a tactical vest holding a radio"/>
    </svg>
    <div class="academy-name">BRANDEL HOLLOW ACADEMY</div>

    <p class="intro">We provide Corporate Security Officer/Criminal Justice/Police Tactics Training for Private Companies that have a security department and officers.</p>

    <ul class="services">
      <li><svg viewBox="0 0 27 12"><path d="M0 1H19L27 6L19 11H0Z" fill="#2e3192"/></svg>Handcuffing certifications</li>
      <li><svg viewBox="0 0 27 12"><path d="M0 1H19L27 6L19 11H0Z" fill="#2e3192"/></svg>Pepper Spray</li>
      <li><svg viewBox="0 0 27 12"><path d="M0 1H19L27 6L19 11H0Z" fill="#2e3192"/></svg>Compliance Training</li>
      <li><svg viewBox="0 0 27 12"><path d="M0 1H19L27 6L19 11H0Z" fill="#2e3192"/></svg>Instructor Training</li>
      <li><svg viewBox="0 0 27 12"><path d="M0 1H19L27 6L19 11H0Z" fill="#2e3192"/></svg>California Guard Card</li>
    </ul>

    <div class="traits">
      <ul class="col-a">
        <li>Value</li>
        <li>Competitive Edge</li>
        <li>Professional Growth</li>
        <li>Quality</li>
        <li>Proficient/Effective Security Officers</li>
      </ul>
      <ul class="col-b">
        <li>Tactical Officers</li>
        <li>Professionalism</li>
        <li>Experts</li>
        <li>Industry Leaders</li>
        <li>Readiness</li>
      </ul>
    </div>

    <address class="contact" style="font-style:normal">
      2180 Fenmore Ave, #214<br>
      Larkwood, CA 90517 | (555) 014-2290<br>
      <span class="web">www.brandelhollowacademy.org</span>
    </address>

    <div class="stamp"></div>
    <div class="address-line" style="top:781px"></div>
    <div class="address-line" style="top:838px"></div>
    <div class="address-line" style="top:895px"></div>

    <svg class="partners" width="270" height="82" viewBox="0 0 270 82" xmlns="http://www.w3.org/2000/svg" role="img" aria-label="Partner certification badges">
      <path d="M8 4H82V44Q82 70 45 80Q8 70 8 44Z" fill="#c8202a"/>
      <rect x="110" y="2" width="68" height="78" fill="#0d0d10"/>
      <path d="M196 12H262V46Q262 66 229 78Q196 66 196 46Z" fill="#c9c9cc"/>
    </svg>
  </main>
</body>
</html>
```